Business Card Design Project

Looking to update our business cards. We have a logo with our slogan. We are an IT firm so we wouldlike a modern look.

Industry/Entity Type

Business

```html
<!DOCTYPE html>
<html lang="en">
<head>
<meta charset="utf-8">
<title>Kinetra – Business Cards</title>
<link href="https://fonts.googleapis.com/css2?family=Questrial&display=swap" rel="stylesheet">
<style>
  :root {
    --backdrop: #e4e2de;
    --card: #ffffff;
    --olive: #5b6f1c;
    --leaf: #4f9a2c;
    --ink: #1f1f1f;
    --shadow: rgba(0, 0, 0, 0.22);
  }
  * { margin: 0; padding: 0; box-sizing: border-box; }
  html, body {
    width: 1200px;
    height: 803px;
    overflow: hidden;
    background: var(--backdrop);
    font-family: "Questrial", sans-serif;
  }
  .stage {
    position: relative;
    width: 1200px;
    height: 803px;
  }
  .card {
    position: absolute;
    width: 620px;
    height: 354px;
    background: var(--card);
    box-shadow: 0 10px 24px var(--shadow);
  }
  .card-front {
    left: 55px;
    top: 70px;
  }
  .card-back {
    left: 525px;
    top: 385px;
  }
  .brand {
    position: absolute;
    left: 0;
    right: 0;
    top: 128px;
    display: flex;
    flex-direction: column;
    align-items: center;
  }
  .brand-name {
    display: flex;
    align-items: center;
    gap: 14px;
    font-size: 58px;
    letter-spacing: 10px;
    color: var(--olive);
    line-height: 1;
  }
  .brand-dot {
    width: 16px;
    height: 16px;
    border-radius: 50%;
    background: var(--olive);
  }
  .tagline {
    margin-top: 14px;
    font-size: 16px;
    letter-spacing: 4.2px;
    color: var(--ink);
  }
  .contact-list {
    position: absolute;
    left: 175px;
    top: 120px;
    list-style: none;
  }
  .contact-item {
    display: flex;
    align-items: center;
    gap: 10px;
    font-size: 20px;
    color: var(--ink);
    line-height: 28px;
    letter-spacing: 0.5px;
    white-space: nowrap;
  }
  .contact-icon {
    width: 16px;
    height: 18px;
    flex: none;
  }
</style>
</head>
<body>
<main class="stage">

  <section class="card card-front" aria-label="Business card front">
    <div class="brand">
      <div class="brand-name"><span class="brand-dot"></span>KINETRA</div>
      <p class="tagline">MAKING TECH WORK BETTER</p>
    </div>
  </section>

  <section class="card card-back" aria-label="Business card back">
    <ul class="contact-list">
      <li class="contact-item">
        <svg class="contact-icon" viewBox="0 0 16 18" aria-hidden="true">
          <rect x="4" y="1" width="8" height="16" rx="1.5" fill="none" stroke="var(--leaf)" stroke-width="1.6"/>
          <rect x="5.5" y="3" width="5" height="5" fill="var(--leaf)"/>
          <circle cx="8" cy="13.5" r="1.2" fill="var(--leaf)"/>
        </svg>
        48-512-907
      </li>
      <li class="contact-item">
        <svg class="contact-icon" viewBox="0 0 16 18" aria-hidden="true">
          <rect x="1" y="3" width="14" height="10" rx="1" fill="none" stroke="var(--leaf)" stroke-width="1.6"/>
          <rect x="6" y="13" width="4" height="2" fill="var(--leaf)"/>
          <rect x="4" y="15" width="8" height="1.6" fill="var(--leaf)"/>
        </svg>
        kinetra.net
      </li>
      <li class="contact-item">
        <svg class="contact-icon" viewBox="0 0 16 18" aria-hidden="true">
          <text x="8" y="14" text-anchor="middle" font-size="16" font-weight="bold" font-family="Arial, sans-serif" fill="var(--leaf)">@</text>
        </svg>
        hello@kinetra.net
      </li>
      <li class="contact-item">
        <svg class="contact-icon" viewBox="0 0 16 18" aria-hidden="true">
          <circle cx="8" cy="9" r="6.5" fill="none" stroke="var(--leaf)" stroke-width="1.6"/>
          <circle cx="8" cy="9" r="2.6" fill="var(--leaf)"/>
        </svg>
        218 Maple Ln, Ardenvale, IL 60410-2291
      </li>
    </ul>
  </section>

</main>
</body>
</html>
```